User profile management app in Bootstrap & AngularJS

We have a single page web app with front end built on AngularJS and Bootstrap. There is a navbar on top and about 10 different views (user profile view, user profile edit, update-able list of items, help section, ...). At this point the app has functionality but no graphics or thought-out layout.

Need a designer to take the existing HTML, CSS (or even JS) files and modify and expand them to make the app look good. Find the existing HTML and JS files for the client attached. You'll need to download angular, bootstrap and ng-map libraries separately.

You can experience the code live at https://design.kelvo.net/kelvoportal.html

The templates provided are text-only but the result should contain a few icons for better visual experience. Some suggested areas for images include device types (email, cell phone, pager, landline phone, ...), status indicators (true/false, on/off, enabled/disabled, ...), navigation (expand/collapse, previous page/next page, ...), file download, CRUD management (add, edit, delete), help popups, etc

The resulting design and code should be mobile-friendly and handicap-accessible (Section 508 compliant).

Font desired: Univers family but not required, otherwise Arial
Only use color from the list provided in the attached file. Colors should not indicate a specific meaning and the whole design should be primarily blue (RGB R0 G103 B198) and white themed.

Allow for banner somewhere on top of page - about 530 x 100 pixels. Allow for a footer with an image on the left and 2-3 sentences of text (copyright, disclaimer, etc).
Updates

Target Market(s)

general public, design for simplicity and ease of use

Industry/Entity Type

Cell Phone

Coding

Coded - Design and coding required

Number of Pages Required

5+ page

Font styles to use
Sans Serif
Other font styles liked:
• Univers family preferred not required otw Arial

Requirements
Must have
• Use blue (RGB R0 G103 B198) and white theme. Must be mobile friendly and handicap-enabled.
• Icons: Use the three stroke weights; light, medium, bold.
• Icons can be designed as outlines or solid silhouettes in two-dimensional form. Icons must be recognizable to a majority of the intended audience. Avoid fine lines and overly complex imagery.

```html
<!DOCTYPE html>
<html lang="en">
<head>
<meta charset="utf-8">
<title>Kelvo Portal – Home</title>
<link href="https://fonts.googleapis.com/css2?family=Open+Sans:wght@400;600;700&display=swap" rel="stylesheet">
<style>
:root{
  --blue:#0067c6;
  --blue-dark:#00509a;
  --blue-tint:#e8f1fa;
  --blue-soft:#f3f8fd;
  --ink:#333333;
  --ink-soft:#4a4a4a;
  --muted:#9aa4ae;
  --white:#ffffff;
  --line:#d6e2ee;
  --banner:#3d8ad4;
}
*{box-sizing:border-box;margin:0;padding:0}
html,body{width:970px;height:1200px;overflow:hidden}
body{position:relative;background:var(--white);font-family:"Open Sans",Arial,sans-serif;color:var(--ink);font-size:16px}
.topbar{height:110px;background:var(--blue);display:flex;align-items:center;justify-content:space-between;padding:0 14px}
.brand{color:var(--white);font-weight:700;font-size:24px;letter-spacing:.3px;width:120px}
.banner{width:530px;height:100px;background:linear-gradient(135deg,var(--banner),var(--blue-dark));border-radius:4px}
.menu-toggle{width:51px;height:36px;border:1px solid var(--white);border-radius:4px;background:var(--blue-dark);display:flex;flex-direction:column;justify-content:center;align-items:center;gap:4px}
.menu-toggle span{display:block;width:22px;height:3px;background:var(--white);border-radius:1px}
.tabs{height:78px;background:var(--white);display:flex;border-bottom:1px solid var(--line)}
.tab{width:115px;border-right:1px solid var(--line);display:flex;flex-direction:column;align-items:center;justify-content:center;gap:6px;color:var(--muted);font-size:15.5px}
.tab.wide{width:138px}
.tab svg{width:22px;height:22px;fill:var(--muted)}
.tab.active{color:var(--blue);font-weight:700;border-bottom:3px solid var(--blue);font-size:15px}
.tab.active svg{fill:var(--blue)}
.content{padding:24px 28px 0}
.panel{background:var(--white);border:1px solid var(--line);border-radius:5px;overflow:hidden;margin-bottom:24px}
.panel-head{height:52px;background:var(--blue-tint);border-bottom:1px solid var(--line);display:flex;align-items:center;padding:0 14px;font-size:19px;color:var(--blue-dark)}
.panel-head svg{width:19px;height:19px;fill:var(--blue);margin-right:14px}
.panel-head .send{margin-left:auto;background:var(--blue);color:var(--white);border:none;border-radius:4px;font:400 18px "Open Sans",Arial,sans-serif;padding:0 17px;height:36px}
table{width:100%;border-collapse:collapse;table-layout:fixed}
th{height:44px;background:var(--blue-soft);font-size:12px;font-weight:600;text-transform:uppercase;text-align:left;padding:0 10px;border-right:1px solid var(--line);border-bottom:1px solid var(--line);color:var(--ink-soft)}
td{height:44px;padding:0 10px;border-right:1px solid var(--line);border-top:1px solid var(--line);font-size:16px}
th:last-child,td:last-child{border-right:none}
tbody tr:nth-child(odd) td{background:var(--blue-soft)}
.profile td{height:67px;line-height:1.4}
.footer{position:absolute;left:0;top:1070px;width:970px;height:130px;background:var(--blue);color:var(--white);font-size:15px;display:flex;align-items:center;justify-content:center}
.footer-image{position:absolute;left:28px;top:25px;width:80px;height:80px;background:linear-gradient(135deg,var(--banner),var(--blue-dark));border-radius:4px}
</style>
</head>
<body>
<header class="topbar">
  <span class="brand">BRAND</span>
  <div class="banner" role="img" aria-label="Banner image area"></div>
  <div class="menu-toggle" aria-label="Menu"><span></span><span></span><span></span></div>
</header>
<nav class="tabs">
  <div class="tab active"><svg viewBox="0 0 24 24"><path d="M12 3 1 12h3v9h6v-6h4v6h6v-9h3z"/></svg>Home</div>
  <div class="tab"><svg viewBox="0 0 24 24"><path d="M2 4h20v16H2zM4 8v10h16V8zm2 2h12v2H6zm0 4h12v2H6z"/></svg>Devices</div>
  <div class="tab"><svg viewBox="0 0 24 24"><path d="M12 2a7 7 0 0 0-7 7c0 5 7 13 7 13s7-8 7-13a7 7 0 0 0-7-7zm0 10a3 3 0 1 1 0-6 3 3 0 0 1 0 6z"/></svg>Locations</div>
  <div class="tab"><svg viewBox="0 0 24 24"><circle cx="12" cy="7" r="5"/><path d="M3 22c0-6 4-9 9-9s9 3 9 9z"/></svg>Profile</div>
  <div class="tab wide"><svg viewBox="0 0 24 24"><circle cx="5" cy="19" r="3"/><path d="M2 9v4a9 9 0 0 1 9 9h4A13 13 0 0 0 2 9zm0-7v4a16 16 0 0 1 16 16h4A20 20 0 0 0 2 2z"/></svg>Subscriptions</div>
  <div class="tab"><svg viewBox="0 0 24 24"><path d="M12 1a11 11 0 1 0 0 22 11 11 0 0 0 0-22zm-1.5 5h3l-.5 8h-2zm1.5 10a2 2 0 1 1 0 4 2 2 0 0 1 0-4z"/></svg>Alert Log</div>
  <div class="tab"><svg viewBox="0 0 24 24"><path d="M12 1a11 11 0 1 0 0 22 11 11 0 0 0 0-22zm1 18h-2.5v-2.5H13zm2.2-7.3c-1.2 1-2.2 1.5-2.2 3.3h-2.5c0-2.8 1.6-3.5 2.6-4.3.7-.6 1-1 1-1.7a2 2 0 0 0-4 0H7.5a4.5 4.5 0 0 1 9 0c0 1.2-.5 2-1.3 2.7z"/></svg>Help</div>
</nav>
<main class="content">
  <section class="panel">
    <div class="panel-head"><svg viewBox="0 0 24 24"><circle cx="12" cy="7" r="5"/><path d="M3 22c0-6 4-9 9-9s9 3 9 9z"/></svg>User Profile</div>
    <table class="profile">
      <colgroup><col style="width:125px"><col style="width:121px"><col style="width:213px"><col style="width:110px"><col style="width:217px"><col></colgroup>
      <thead><tr><th>First Name</th><th>Last Name</th><th>Email Address</th><th>City</th><th>State</th><th>Languages</th></tr></thead>
      <tbody><tr><td>Dan</td><td>Porter</td><td>admin@inboxly.com</td><td>Gotham</td><td>AMERICAN SAMOA</td><td>French<br>Spanish</td></tr></tbody>
    </table>
  </section>
  <section class="panel">
    <div class="panel-head"><svg viewBox="0 0 26 24"><circle cx="13" cy="7" r="4"/><circle cx="5" cy="9" r="3"/><circle cx="21" cy="9" r="3"/><path d="M6 21c0-5 3-8 7-8s7 3 7 8zM0 19c0-4 2-6 5-6 1 0 2 .3 2.5.8C6 15 5 17 5 19zM26 19c0-4-2-6-5-6-1 0-2 .3-2.5.8C20 15 21 17 21 19z"/></svg>Groups</div>
    <table>
      <colgroup><col style="width:277px"><col style="width:294px"><col></colgroup>
      <thead><tr><th>Group Name</th><th>Category</th><th>Type</th></tr></thead>
      <tbody>
        <tr><td>Group One</td><td>Category Top</td><td>Group Type Top</td></tr>
        <tr><td>Group Two</td><td>Category Top</td><td>Group Type Top</td></tr>
        <tr><td>Group Three</td><td>Category Top</td><td>Group Type Top</td></tr>
        <tr><td>Group Four</td><td>Category Top</td><td>Group Type Top</td></tr>
        <tr><td>Group Five</td><td>Category Top</td><td>Group Type Top</td></tr>
      </tbody>
    </table>
  </section>
  <section class="panel">
    <div class="panel-head"><svg viewBox="0 0 24 24"><path d="M2 4h20v16H2zM4 8v10h16V8zm2 2h12v2H6zm0 4h12v2H6z"/></svg>Devices<button class="send">Send</button></div>
    <table>
      <colgroup><col style="width:428px"><col style="width:308px"><col></colgroup>
      <thead><tr><th>Device Identifier</th><th>Delivery Channel</th><th>Status</th></tr></thead>
      <tbody>
        <tr><td>danporter@norvale.com</td><td>E-mail account</td><td>Enabled</td></tr>
        <tr><td>(123)456-7890</td><td>telnova</td><td>Enabled</td></tr>
        <tr><td>danporter@norvale.com2</td><td>E-mail account</td><td>Alias</td></tr>
        <tr><td>qwrtyq@qwrty.com</td><td>E-mail account</td><td>Enabled</td></tr>
      </tbody>
    </table>
  </section>
</main>
<footer class="footer">
  <div class="footer-image" role="img" aria-label="Footer image area"></div>
  © 2015 Brand. All right reserved.
</footer>
</body>
</html>
```